Residential Construction Business - Site Signage

I need a design made for a site fence banner. We have a logo and branding so the design would need to be aligned with this. It would need to be made to specific size ratio so that it can be sent to the maker for production.
ratio : 4600 wide x 1700 high
The design should feature our website and also the slogan
"STAY PUT, BUILD BETTER"

Target Market(s)

potential clients

Industry/Entity Type

construction

Font styles to use
Other font styles liked:
• to match branding

Colors
0054AA
0677BA
7BADD7
CADEEF
E8F1F8

Requirements
Must have
• www.velmarbuild.com.au Majority of the sign is our brand logo
Nice to have
• Majority of the sign is our brand logo
Should not have
• colors and themes that arent brand relevant

```html
<!DOCTYPE html>
<html lang="en">
<head>
<meta charset="utf-8">
<title>Velmar Build – Site Fence Banner</title>
<link rel="stylesheet" href="https://fonts.googleapis.com/css2?family=Montserrat:wght@400;600;700&display=swap">
<style>
  :root {
    --stage: #d9d9dc;
    --brand-navy: #053d5e;
    --banner-light: #f2f2f5;
    --web-grey: #7d9bb0;
    --rule: #a9b8c6;
  }
  html, body {
    margin: 0;
    padding: 0;
    width: 1200px;
    height: 518px;
    overflow: hidden;
    background: var(--stage);
  }
  .canvas {
    position: relative;
    width: 1200px;
    height: 518px;
  }
  .fence-banner {
    position: absolute;
    left: 59px;
    top: 52px;
    width: 1081px;
    height: 399px;
    display: block;
    font-family: "Montserrat", Arial, sans-serif;
  }
  .banner-base { fill: var(--banner-light); }
  .brand-chevron { fill: var(--brand-navy); }
  .website { fill: var(--web-grey); font-size: 27px; font-weight: 700; }
  .website-tld { font-weight: 400; }
  .brand-name { fill: var(--brand-navy); font-size: 64px; font-weight: 600; }
  .slogan { fill: var(--brand-navy); font-size: 28px; font-weight: 700; }
  .slogan-rule { stroke: var(--rule); stroke-width: 1.2; }
</style>
</head>
<body>
  <main class="canvas">
    <svg class="fence-banner" viewBox="0 0 1081 399" xmlns="http://www.w3.org/2000/svg" role="img" aria-label="Velmar Build site fence banner">
      <rect class="banner-base" x="0" y="0" width="1081" height="399"/>
      <path class="brand-chevron" d="M0 0 H523 L374 160 Q360.5 176 360.5 197.5 Q360.5 220 375 235 L537 399 H0 Z"/>

      <text class="website" x="1007" y="93" text-anchor="end">velmarbuild.com<tspan class="website-tld">.au</tspan></text>

      <text class="brand-name" x="389" y="223" textLength="620" lengthAdjust="spacing">VELMAR BUILD</text>

      <line class="slogan-rule" x1="545" y1="257" x2="1007" y2="257"/>
      <text class="slogan" x="545" y="294" textLength="462" lengthAdjust="spacingAndGlyphs">STAY PUT, BUILD BETTER</text>
      <line class="slogan-rule" x1="545" y1="308" x2="1007" y2="308"/>
    </svg>
  </main>
</body>
</html>
```